Web Design Brochure

We want a brochure, that we can email and also be sent to our printers. I've attached our logo and content for the brochure. Our websites are www.velmora.co.uk and www.velmora-franchise.co.uk
We would want the source files as part of the deal.
Updates

We only need a nice simple design. Just one brochure not an email aswell. We can email the brochure. We have a number of designers in house who are tied up on a big project. They tell me they could put something together in an hour or so. So £30 we feel is ample for a quick and simple project.

Target Market(s)

businesses

Industry/Entity Type

Advertising

```html
<!DOCTYPE html>
<html lang="en">
<head>
<meta charset="utf-8">
<title>Velmora Web Design Brochure</title>
<link rel="stylesheet" href="https://fonts.googleapis.com/css2?family=Arimo:wght@400;700&display=swap">
<style>
  :root {
    --page-white: #ffffff;
    --violet-deep: #3a0ff2;
    --violet-mid: #5a18e8;
    --magenta: #a42ac4;
    --flame: #ff4a1c;
    --text-light: #f6d6ff;
    --heading-red: #ff4a2a;
    --logo-ink: #1c1a2b;
    --logo-mark: #7a3cf0;
    --spine: #2a1a3a;
  }
  * { margin: 0; padding: 0; box-sizing: border-box; }
  html, body { width: 1059px; height: 1200px; overflow: hidden; background: var(--page-white); }
  .canvas { position: relative; width: 1059px; height: 1200px; overflow: hidden; background: var(--page-white); font-family: "Arimo", Arial, sans-serif; }

  .spread { position: absolute; left: 176px; width: 701px; overflow: hidden; }
  .cover-spread { top: 87px; height: 497px; }
  .inside-spread { top: 621px; height: 494px; background: var(--violet-deep); box-shadow: 4px 5px 6px rgba(0,0,0,0.45); }

  .cover-backdrop {
    position: absolute; inset: 0;
    background: radial-gradient(ellipse 420px 380px at 350px 0, var(--flame) 0%, var(--magenta) 38%, var(--violet-mid) 68%, var(--violet-deep) 100%);
  }
  .spine { position: absolute; left: 350px; top: 0; width: 1.5px; height: 100%; background: var(--spine); }
  .inside-spine { position: absolute; left: 350px; top: 0; width: 1px; height: 100%; background: rgba(255,255,255,0.08); }

  .brand-panel {
    position: absolute; left: 351px; top: 224px; width: 202px; height: 64px;
    background: var(--page-white);
    display: flex; align-items: center; gap: 8px; padding-left: 10px;
  }
  .brand-dot { width: 26px; height: 26px; border-radius: 50%; background: var(--logo-mark); flex: none; }
  .brand-name { font-weight: 700; font-size: 29px; letter-spacing: 1px; color: var(--logo-ink); }

  .page { position: absolute; top: 0; height: 100%; color: var(--text-light); font-size: 6.9px; line-height: 7.6px; }
  .page-left { left: 0; width: 350px; padding: 29px 30px 0 45px; }
  .page-right { left: 351px; width: 350px; padding: 35px 38px 0 50px; }

  .page-title { text-align: center; color: var(--heading-red); font-size: 10.5px; line-height: 12px; font-weight: 700; margin-bottom: 30px; }
  .section-head { color: var(--heading-red); font-weight: 700; font-size: 6.9px; line-height: 8px; margin-bottom: 1px; }
  .fact-list { list-style: disc; padding-left: 24px; margin-bottom: 12px; }
  .reasons-list { list-style: disc; padding-left: 24px; margin: 10px 0 13px; line-height: 10.7px; }
  .standard-list { list-style: disc; padding-left: 24px; margin-top: 12px; line-height: 10.4px; }
  .page-right p { margin-bottom: 8px; }
  .price-line { margin-top: 6px; margin-bottom: 9px; }
  .page-list { list-style: disc; padding-left: 24px; margin: 6px 0 4px; line-height: 9.8px; }
  .feature-list { list-style: disc; padding-left: 24px; margin: 8px 0 6px; line-height: 7.6px; }
  .emphasis { font-weight: 700; }
  .small-note { font-size: 5px; }
</style>
</head>
<body>
<div class="canvas">

  <section class="spread cover-spread" aria-label="Brochure cover spread">
    <div class="cover-backdrop" role="img" aria-label="Cover artwork: soft glow from flame orange at the top centre fading into deep violet"></div>
    <div class="spine"></div>
    <div class="brand-panel">
      <span class="brand-dot"></span>
      <span class="brand-name">VELMORA</span>
    </div>
  </section>

  <section class="spread inside-spread" aria-label="Brochure inside spread">
    <div class="inside-spine"></div>

    <div class="page page-left">
      <h1 class="page-title">Velmora Web Design Packages</h1>

      <h2 class="section-head">The Web</h2>
      <ul class="fact-list">
        <li>All businesses need to advertise and the internet is without doubt the fastest growing advertising medium in the UK.</li>
        <li>Online Consumer spending on goods and services (excluding financial transactions) accelerated to £46.6m in the last year.</li>
        <li>Lookwise, online directories and regional start ups are all taking market share from local newspapers.</li>
        <li>UK internet advertising spend now represents 20% of all advertising spend in the UK.</li>
        <li>The internet and use of websites as the core business marketing tool has grown rapidly over the last five years but is still largely in its infancy.</li>
        <li>There are currently over 2,500,000 small to medium size business in the UK and only 50 % of these small to medium size businesses actually have a web presence.</li>
        <li>Over 7,000 new businesses start up every month in the UK.</li>
        <li>The internet is now more popular than TV in UK households.</li>
      </ul>

      <h2 class="section-head">Why choose Velmora?</h2>
      <ul class="reasons-list">
        <li>No longer need to rely on expensive web companies to edit or change your website</li>
        <li>Absolutely no technical experience needed!</li>
        <li>Editing is as easy as using Scribewell Writer</li>
        <li>All sites are expertly designed</li>
        <li>Edit from ANY browser on any computer with no need to install software - it's just like Writer or desk - top publishing</li>
        <li>Very affordable for clients with 'easy payment' terms starting at just over £1 per day!</li>
      </ul>

      <h2 class="section-head">ALL SITES INCLUDE AS STANDARD</h2>
      <ul class="standard-list">
        <li>Initial marketing and design consultancy</li>
        <li>Home page design with designed navigation, images and link</li>
        <li>About us page</li>
        <li>Contact page with contact form</li>
        <li>Plus 2 other pages for products, services or information</li>
        <li>Domain name transfer</li>
        <li>High band width, Secure server business hosting with failsafe back up</li>
        <li>Corporate e-mail addresses</li>
        <li>Full optimisation for search engines built in</li>
        <li>Registration with search engines</li>
        <li>Lookwise Insights (statistics on visits to your site)</li>
        <li>Website Hosting</li>
      </ul>
    </div>

    <div class="page page-right">
      <h2 class="section-head">Websites</h2>
      <p class="price-line">1/2 page website £200 or £20pm</p>
      <p>Brilliant for creating simple professional business website to personal interest and <span class="small-note">hobby web pages</span> or even selling a property<br>4/5 page brochure style website £500 or £35pm</p>
      <ul class="page-list">
        <li>Home Page</li>
        <li>Products page</li>
        <li>services page</li>
        <li>About us page</li>
        <li>Contact us page</li>
      </ul>
      <p>'Brochure Style' refers to a basic HTML website or basic website design. A simple website will provide your client with an online web presence. Brochure style website design can be tailored to your clients exact requirement and provide their business with an entry level website platform to showcase their products or services online. You can be as innovative and creative as you desire with this basic website</p>
      <p>Additional Functionality £100 or £10pm</p>
      <p>Additional functionality such as basic forums and blogs are available at £100 or £10 per month. Any advanced functionality would fall into our bespoke packages.</p>
      <p>Ecommerce Website £1000</p>
      <p>Our scalable custom built online store ecommerce solutions can incorporate the following features based on customer's requirements.</p>
      <ul class="feature-list">
        <li>Allows your customer to browse a limitless number of online products and product categories.</li>
        <li>Customers can add/remove and modify products to their online shopping cart.</li>
        <li>Intuitive checkout system minimizes online shopping cart abandonment.</li>
        <li>Automatically generates and emails a Tax Invoice to your customer.</li>
        <li>SSL 128bit encryption for secure online transactions.</li>
        <li>Complete online inventory management along with ecommerce.</li>
        <li>Online order management systems.</li>
        <li>Third party payment gateway integration with the ecommerce system.</li>
        <li>Search Engine friendly catalogues and content management systems</li>
      </ul>
      <p>Display featured products with an image, price, strap line and short description. Choose which products you would like displayed and how they should be arranged. Whatever you call it; shopping online, e-Commerce, web purchasing... buying products, services and electronic downloads via a website is a growing business.</p>
      <p class="emphasis">The only definite thing that will happen to online purchases is that they will continue to grow over the coming years</p>
      <p class="emphasis">Bespoke website £negotiable prices start from £1000</p>
      <p>Bespoke websites cover a whole spectrum of different styles of including Social networking site, forums, blogs.</p>
    </div>
  </section>

</div>
</body>
</html>
```